Insurance company needs a business card design

We need a business card design for a Massachusetts-based insurance company Veloria Insurance, LLC. We provide auto insurance to Hispanic (Spanish- or Portuguese-speaking) immigrants in the United States. We will give these business cards to auto dealers where such customers typically go to purchase vehicles. We will provide a solution to the dealers to provide easy insurance to the customers buying cars at their dealerships. Veloria is the Spanish word for protection.
Contact Information for Business Card
Name, Designation, Company Name, Address, Phone Number, Email, Website
Look and feel
Each slider illustrates characteristics of the customer's brand and the style your logo design should communicate.

```html
<!DOCTYPE html>
<html lang="en">
<head>
<meta charset="utf-8">
<title>Veloria Insurance — Business Card</title>
<link href="https://fonts.googleapis.com/css2?family=Montserrat:wght@600;700&family=Arimo:wght@400&display=swap" rel="stylesheet">
<style>
  :root {
    --ink-blue: #0b4a80;
    --edge-orange: #f28a1c;
    --accent-orange: #f5891f;
    --paper-white: #ffffff;
    --stage: #2a2a2c;
  }
  html, body {
    margin: 0;
    width: 1200px;
    height: 900px;
    overflow: hidden;
    background: var(--stage);
  }
  .canvas {
    width: 1200px;
    height: 900px;
    display: flex;
    flex-direction: column;
    align-items: center;
    justify-content: center;
    gap: 60px;
  }
  .card {
    position: relative;
    width: 630px;
    height: 360px;
    background: var(--ink-blue);
    border-radius: 22px;
    box-shadow: 0 0 0 3px var(--edge-orange), 0 14px 30px rgba(0,0,0,.5);
    box-sizing: border-box;
  }
  .wordmark {
    display: flex;
    align-items: center;
    gap: 14px;
    font-family: "Montserrat", sans-serif;
    font-weight: 700;
    color: var(--paper-white);
    letter-spacing: .06em;
    text-transform: uppercase;
    line-height: 1;
  }
  .wordmark-square {
    background: var(--accent-orange);
    flex: none;
  }
  .card-front {
    display: flex;
    align-items: center;
    justify-content: center;
  }
  .card-front .wordmark { font-size: 40px; }
  .card-front .wordmark-square { width: 34px; height: 34px; }

  .card-back { padding: 34px 40px; }
  .card-back .wordmark { font-size: 24px; gap: 10px; }
  .card-back .wordmark-square { width: 20px; height: 20px; }

  .person {
    margin-top: 44px;
    padding-left: 18px;
    border-left: 6px solid var(--accent-orange);
  }
  .person-name {
    font-family: "Montserrat", sans-serif;
    font-weight: 700;
    font-size: 30px;
    letter-spacing: .05em;
    color: var(--accent-orange);
    margin: 0;
    line-height: 1.1;
  }
  .person-title {
    font-family: "Arimo", sans-serif;
    font-size: 17px;
    color: var(--paper-white);
    margin: 4px 0 0;
  }
  .address {
    font-family: "Arimo", sans-serif;
    font-size: 17px;
    color: var(--paper-white);
    font-style: normal;
    line-height: 1.35;
    margin: 18px 0 0 24px;
  }
  .contact-list {
    list-style: none;
    margin: 16px 0 0 24px;
    padding: 0;
    font-family: "Arimo", sans-serif;
    font-size: 17px;
    color: var(--paper-white);
  }
  .contact-list li {
    display: flex;
    align-items: center;
    gap: 12px;
    line-height: 1.55;
  }
  .contact-icon { width: 16px; height: 16px; flex: none; }
</style>
</head>
<body>
<main class="canvas">
  <section class="card card-front" aria-label="Card front">
    <div class="wordmark"><span class="wordmark-square"></span>Veloria Insurance</div>
  </section>

  <section class="card card-back" aria-label="Card back">
    <div class="wordmark"><span class="wordmark-square"></span>Veloria Insurance</div>
    <div class="person">
      <h1 class="person-name">DANIEL REYES</h1>
      <p class="person-title">Managing Director</p>
    </div>
    <address class="address">4120 Harbor Street<br>Boston, MA 02118</address>
    <ul class="contact-list">
      <li>
        <svg class="contact-icon" viewBox="0 0 16 16" aria-hidden="true"><path fill="#f5891f" d="M3.6 1.5l2.2 2.6-1.2 1.7c.9 2 2.6 3.7 4.6 4.6l1.7-1.2 2.6 2.2-1.3 2.3C7 13.4 2.6 9 1.3 2.8z"/></svg>
        (617) 555-0148
      </li>
      <li>
        <svg class="contact-icon" viewBox="0 0 16 16" aria-hidden="true"><rect x="1" y="3.5" width="14" height="9" rx="1" fill="#f5891f"/><path d="M1.5 4.2L8 9l6.5-4.8" stroke="#0b4a80" stroke-width="1.3" fill="none"/></svg>
        info@veloriainsurance.com
      </li>
      <li>
        <svg class="contact-icon" viewBox="0 0 16 16" aria-hidden="true"><circle cx="8" cy="8" r="6.5" fill="none" stroke="#f5891f" stroke-width="1.5"/><ellipse cx="8" cy="8" rx="2.8" ry="6.5" fill="none" stroke="#f5891f" stroke-width="1.2"/><path d="M1.5 8h13" stroke="#f5891f" stroke-width="1.2"/></svg>
        www.veloriainsurance.com
      </li>
    </ul>
  </section>
</main>
</body>
</html>
```